Company Capability Brochure

Want to create a mulit paged brochure to hand out to potential clients to show our services and capabilities.

Attached is a rough draft we made using chatgpt which can be use as an example and includes the categories, text, our logo and preferred colour scheme we wish to use.
Would like to make this more look more visually appealing and a more professional layout over more pages.

```html
<!DOCTYPE html>
<html lang="en">
<head>
<meta charset="utf-8">
<title>Northgate Security Services – Capability Brochure</title>
<link href="https://fonts.googleapis.com/css2?family=Lato:ital,wght@0,300;0,400;0,700;0,900;1,300&display=swap" rel="stylesheet">
<style>
:root{
  --stage:#ececec;
  --paper:#ffffff;
  --navy:#2b3aa0;
  --sky:#29abe2;
  --sky-pale:#c4e6f6;
  --ink:#1f1f2b;
  --deep:#1d1b47;
  --rule:#4fb4e4;
}
*{box-sizing:border-box;margin:0;padding:0}
html,body{width:1200px;height:1200px;overflow:hidden;background:var(--stage);font-family:'Lato',sans-serif;color:var(--ink)}
.spread{position:absolute;width:489px;height:346px;background:var(--paper);overflow:hidden;box-shadow:0 2px 5px rgba(0,0,0,.18)}
.spread--cover{left:92px;top:232px}
.spread--vision{left:619px;top:232px}
.spread--culture{left:92px;top:622px}
.spread--services{left:619px;top:622px}
.abs{position:absolute}
.brand{display:flex;align-items:center;gap:5px}
.brand__dot{width:18px;height:18px;border-radius:50%;background:var(--sky)}
.brand__name{font-weight:900;color:var(--sky);letter-spacing:2px;line-height:1}
.page-rule{position:absolute;left:23px;right:23px;top:332px;height:1px;background:var(--rule)}
.page-num{position:absolute;top:329px;font-size:4px;color:#444}

/* cover */
.cover__band{left:0;top:171px;width:489px;height:175px;background:linear-gradient(180deg,#1b9fe0 0%,#2366c8 50%,#2b3aa0 100%)}
.cover__headline{left:280px;top:90px;font-size:15.5px;line-height:19px;font-weight:700;color:var(--sky)}
.cover__headline span{color:var(--navy)}
.cover__quote{left:35px;top:209px;font-size:11px;line-height:16px;font-style:italic;font-weight:300;color:#fff}
.cover__contact{left:35px;top:264px;color:#fff;font-size:5px;line-height:8px}
.cover__contact .label{font-size:5px;letter-spacing:.3px}
.cover__contact .company{font-size:7px;font-weight:700;margin-bottom:4px}
.cover__contact .row{display:flex;align-items:center;gap:4px;margin-left:-9px}
.cover__contact svg{width:5px;height:5px}
.cover__license{left:280px;top:314px;font-size:6px;color:#cfe9ff}
.cover__rule{left:0;right:0;top:332px;height:1px;background:#5fb6ea}

/* statements */
.statement__big{font-size:25px;font-weight:400;color:var(--sky-pale);letter-spacing:-.5px;line-height:1}
.statement__small{font-size:8.5px;letter-spacing:2px;color:var(--navy);font-weight:400}
.statement__body{font-size:4.9px;line-height:7.8px;width:130px}
.vision__box{left:36px;top:212px;width:244px;height:106px;background:var(--sky)}
.vision__img{left:280px;top:60px;width:210px;height:256px;background:radial-gradient(circle at 40% 45%,#2f6fb5 0%,#163a6e 35%,#0b1a35 75%)}

/* culture */
.culture__img{left:0;top:0;width:302px;height:291px;background:linear-gradient(120deg,#2b2a5e 0%,#1d1b47 55%,#3a3560 100%)}
.culture__title{left:36px;top:93px;font-size:24px;font-weight:700;color:var(--sky);letter-spacing:.5px}
.culture__sub{left:99px;top:124px;font-size:8.5px;letter-spacing:2px;color:#fff}
.culture__bar{left:209px;top:113px;width:93px;height:233px;background:linear-gradient(180deg,var(--navy) 0%,#1f7fd3 70%,#1aa3e0 100%)}
.culture__body{left:326px;top:124px;width:118px;font-size:4.9px;line-height:7.8px}
.culture__body p{margin-bottom:3.5px}

/* services */
.services__title{left:76px;top:40px;display:flex;align-items:baseline;gap:5px}
.services__title .big{font-size:24px;color:var(--sky-pale);line-height:1}
.services__title .small{font-size:8.5px;letter-spacing:1.8px;color:var(--navy)}
.service{position:absolute;left:23px;width:198px;display:flex}
.service__name{width:54px;font-size:7px;line-height:8.5px;color:var(--sky)}
.service__list{width:144px;font-size:3.4px;line-height:4.3px;padding-left:5px}
.service__list li{margin-bottom:1.3px}
.service-rule{position:absolute;left:23px;width:198px;height:1px;background:var(--rule)}
.clients__panel{left:244px;top:0;width:245px;height:346px;background:linear-gradient(180deg,#1aa3e0 0%,#2468c7 50%,#2b3aa0 100%)}
.clients__title{left:280px;top:40px;display:flex;align-items:baseline;gap:5px;color:#fff}
.clients__title .big{font-size:24px;line-height:1}
.clients__title .small{font-size:8.5px;letter-spacing:1.8px}
.clients__card{left:273px;top:77px;width:186px;height:232px;background:#fff;border-radius:10px;display:grid;grid-template-columns:1fr 1fr;grid-template-rows:repeat(5,1fr);padding:10px 8px;align-items:center;justify-items:center}
.client{font-size:8px;font-weight:700;color:var(--navy);text-align:center;display:flex;align-items:center;gap:3px}
.client__sq{width:6px;height:6px;background:var(--sky)}
.client__ci{width:7px;height:7px;border-radius:50%;background:#d8302f}
</style>
</head>
<body>

<!-- cover spread -->
<section class="spread spread--cover">
  <div class="abs brand" style="left:52px;top:66px">
    <span class="brand__dot"></span><span class="brand__name" style="font-size:12px">NORTHGATE</span>
  </div>
  <div class="abs brand" style="left:280px;top:30px">
    <span class="brand__dot" style="width:22px;height:22px"></span><span class="brand__name" style="font-size:14px">NORTHGATE</span>
  </div>
  <h1 class="abs cover__headline"><span>Be Informed and</span><br>Make the Right<br>Choice</h1>
  <div class="abs cover__band" role="img" aria-label="Photo of a security camera over a blue building facade"></div>
  <p class="abs cover__quote">‘Be Informed and<br>Make The Right Choice”</p>
  <div class="abs cover__contact">
    <div class="label">CONTACT US</div>
    <div class="company">Northgate Security Services</div>
    <div class="row"><svg viewBox="0 0 10 10"><path d="M2 1l2 2-1 1.5a6 6 0 0 0 2.5 2.5L7 6l2 2-1.5 1.5C4.5 9 1 5.5.5 2.5z" fill="#7fd0ff"/></svg>1300 555 019</div>
    <div class="row"><svg viewBox="0 0 10 10"><rect x="1" y="2.5" width="8" height="5" fill="#7fd0ff"/></svg>info@northgatesecurity.com.au</div>
    <div class="row"><svg viewBox="0 0 10 10"><path d="M5 .5a3.5 3.5 0 0 1 3.5 3.5C8.5 7 5 9.5 5 9.5S1.5 7 1.5 4A3.5 3.5 0 0 1 5 .5z" fill="#7fd0ff"/></svg>12/8 Harbour Ln, Kingsford, NSW 2032</div>
    <div class="row" style="margin-top:4px"><svg viewBox="0 0 10 10"><circle cx="5" cy="5" r="4" fill="#7fd0ff"/></svg>www.northgatesecurity.com.au</div>
  </div>
  <div class="abs cover__license">Master License: 418265037</div>
  <div class="abs cover__rule"></div>
</section>

<!-- vision & mission spread -->
<section class="spread spread--vision">
  <div class="abs statement__big" style="left:37px;top:40px">VISION</div>
  <div class="abs statement__small" style="left:98px;top:53px">STATEMENT</div>
  <p class="abs statement__body" style="left:81px;top:73px">Our mission is to deliver exceptional service and cutting-edge Electronic and Mechanical Security Solutions that not only meet but consistently exceed our clients’ expectations. We are dedicated to ensuring the safety, protection, and peace of mind of those we serve by combining advanced technologies, industry expertise, and a relentless focus on quality, reliability, and customer satisfaction. Through personalized solutions, responsive support, and continuous innovation, we aim to build long-term partnerships and be a trusted name in security.</p>
  <div class="abs statement__big" style="left:37px;top:184px">MISION</div>
  <div class="abs statement__small" style="left:98px;top:196px">STATEMENT</div>
  <div class="abs vision__box"></div>
  <p class="abs statement__body" style="left:81px;top:222px;color:#fff">Our vision is to be the most trusted, innovative, and customer-focused partner in the security industry, renowned for the professional installation, service, and maintenance of Electronic and Mechanical Security Systems. We strive to set the benchmark for excellence by delivering tailored, reliable, and future-ready solutions that protect what matters most to our clients, while building lasting relationships based on integrity, responsiveness, and continuous improvement.</p>
  <div class="abs vision__img" role="img" aria-label="Illustration of a glowing digital security interface with lock and shield icons"></div>
  <div class="page-rule"></div>
  <span class="page-num" style="left:15px">1</span>
  <span class="page-num" style="right:15px">2</span>
</section>

<!-- culture spread -->
<section class="spread spread--culture">
  <div class="abs culture__img" role="img" aria-label="Photo of a hand holding an access card to a door reader"></div>
  <h2 class="abs culture__title">CULTURE</h2>
  <div class="abs culture__sub">STATEMENT</div>
  <div class="abs culture__bar"></div>
  <div class="abs culture__body">
    <p>At the heart of our company is a culture driven by trust, innovation, and service excellence. We are a team of dedicated professionals who take pride in protecting what matters most to our clients through advanced Electronic and Mechanical Security Solutions.</p>
    <p>We cultivate a work environment built on integrity, mutual respect, and accountability, where every team member is empowered to grow, contribute ideas, and take ownership of outcomes. Collaboration, continuous improvement, and a commitment to exceeding expectations define how we operate-both with our clients and each other.</p>
    <p>We embrace change, champion innovation, and remain agile in an evolving industry-always striving to deliver smarter, more reliable, and more secure solutions. Together, we are building not just systems, but lasting partnerships and a safer future.</p>
  </div>
  <div class="page-rule" style="left:23px;right:23px"></div>
  <span class="page-num" style="left:15px">3</span>
  <span class="page-num" style="right:15px">4</span>
</section>

<!-- services & clients spread -->
<section class="spread spread--services">
  <div class="abs brand" style="left:23px;top:28px">
    <span class="brand__dot" style="width:20px;height:20px"></span>
  </div>
  <div class="abs services__title"><span class="big">OUR</span><span class="small">SERVICES</span></div>

  <div class="service" style="top:82px">
    <div class="service__name">Access<br>Control<br>Solution</div>
    <ul class="service__list">
      <li>Access control gives a higher level of security to residents, staff and the premises by granting entry only to approved users.</li>
      <li>Lets you monitor staff movement and hours, knowing exactly when they enter and leave.</li>
      <li>Strata can keep full control over users and their access levels.</li>
      <li>Allocate individual access to set floors or rooms.</li>
      <li>Removes the problem of keys being cut and shared.</li>
      <li>Easy to disable and replace lost or stolen fobs.</li>
    </ul>
  </div>
  <div class="service-rule" style="top:140px"></div>

  <div class="service" style="top:150px">
    <div class="service__name">CCTV<br>Systems</div>
    <ul class="service__list">
      <li>Protect your home or office against theft and vandalism.</li>
      <li>Monitor the premises against intruders.</li>
      <li>Infrared day and night capability.</li>
      <li>Customised to the needs of each property.</li>
      <li>Remote viewing of cameras.</li>
    </ul>
  </div>
  <div class="service-rule" style="top:184px"></div>

  <div class="service" style="top:194px">
    <div class="service__name">Intercoms<br>Systems</div>
    <ul class="service__list">
      <li>Common in offices and apartments, intercoms link the entry door to an internal handset.</li>
      <li>Our qualified technicians install, service and upgrade intercoms.</li>
      <li>A large range of panels to suit every resident.</li>
    </ul>
  </div>
  <div class="service-rule" style="top:229px"></div>

  <div class="service" style="top:239px">
    <div class="service__name">Alarm<br>Systems</div>
    <ul class="service__list">
      <li>Alarms protect premises against intruders and give peace of mind at home or office.</li>
      <li>Monitoring can be linked with your system to keep premises safe when empty.</li>
      <li>Designed to meet your needs, simple or elaborate.</li>
    </ul>
  </div>
  <div class="service-rule" style="top:274px"></div>

  <div class="service" style="top:284px">
    <div class="service__name">Gates</div>
    <ul class="service__list">
      <li>Ongoing security of your premises with mobile patrols.</li>
      <li>Random or scheduled patrols to suit your needs.</li>
      <li>Alarm monitoring customised for your business.</li>
      <li>24/7/365 alarm monitoring and receiving.</li>
      <li>Response patrols to inspect premises after an alarm.</li>
    </ul>
  </div>

  <div class="abs clients__panel" role="img" aria-label="Blue-tinted photo of a keypad entry panel"></div>
  <div class="abs clients__title"><span class="big">OUR</span><span class="small">CLIENTS</span></div>
  <div class="abs clients__card">
    <div class="client">HARBOURLINE</div>
    <div class="client" style="font-weight:400">westview hotels</div>
    <div class="client"><span class="client__sq"></span>Crestfield College</div>
    <div class="client">APEX</div>
    <div class="client">brook &amp; hale</div>
    <div class="client"><span class="client__sq"></span>stratawell</div>
    <div class="client"><span class="client__ci"></span>Meridian Group</div>
    <div class="client">Ridgeway Leagues</div>
    <div class="client">OAKMERE</div>
    <div class="client">Keystone Strata</div>
  </div>
  <div class="page-rule"></div>
  <span class="page-num" style="left:15px">5</span>
  <span class="page-num" style="right:15px;color:#fff">6</span>
</section>

</body>
</html>
```